Modern Design Business Card industrial maintenance company

Business card design for Company named Brookvale Equipment Services

Target Market(s)

Industrial

Industry/Entity Type

Maintenance and repair

Contact Information for Business Card

Place holder for address, office phone, mobile number and email

Requirements
Must have
• Clean modern look
Nice to have
• N/a

```html
<!DOCTYPE html>
<html lang="en">
<head>
<meta charset="utf-8">
<title>Brookvale Equipment Services – Business Card</title>
<link href="https://fonts.googleapis.com/css2?family=Montserrat:wght@400;500;600;700&display=swap" rel="stylesheet">
<style>
  :root {
    --ink: #0a0a0a;
    --paper: #ffffff;
    --stage: #e9eaec;
    --mid-grey: #7d7d7d;
    --rule: #222222;
  }
  * { box-sizing: border-box; margin: 0; padding: 0; }
  html, body {
    width: 1200px; height: 900px; overflow: hidden;
    background: var(--stage);
    font-family: "Montserrat", sans-serif;
  }
  .canvas {
    width: 1200px; height: 900px;
    display: flex; flex-direction: column; align-items: center; justify-content: center;
    gap: 40px;
  }
  .card {
    width: 700px; height: 400px; position: relative; overflow: hidden;
    box-shadow: 0 2px 6px rgba(0,0,0,.12);
  }
  .card--front { background: var(--ink); color: var(--paper); display: flex; align-items: center; justify-content: center; }
  .card--back { background: var(--paper); color: var(--ink); }

  .brand { display: flex; align-items: center; gap: 18px; }
  .brand__dot {
    width: 58px; height: 58px; border-radius: 50%;
    border: 4px solid currentColor; flex: none;
  }
  .brand__name { font-weight: 600; text-transform: uppercase; line-height: 1.1; }
  .brand__name .line1 { display: block; font-size: 40px; letter-spacing: 2px; }
  .brand__name .line2 { display: block; font-size: 13px; letter-spacing: 6.2px; margin-top: 6px; }

  .card--back .brand { position: absolute; left: 46px; top: 120px; z-index: 2; }
  .card--back .brand__dot { width: 48px; height: 48px; border-width: 3px; }
  .card--back .brand__name .line1 { font-size: 32px; letter-spacing: 1.5px; }
  .card--back .brand__name .line2 { font-size: 10.5px; letter-spacing: 4.8px; margin-top: 5px; }

  .divider {
    position: absolute; left: 392px; top: 64px; width: 1px; height: 186px;
    background: var(--rule); z-index: 2;
  }
  .contact { position: absolute; left: 416px; top: 54px; z-index: 2; }
  .contact__name { font-weight: 700; font-size: 30px; line-height: 1.1; }
  .contact__role { font-size: 15px; font-weight: 500; margin-top: 4px; }
  .contact__address { font-size: 15px; font-weight: 500; margin-top: 12px; line-height: 1.35; }
  .contact__list { list-style: none; margin-top: 10px; font-size: 15px; font-weight: 500; }
  .contact__list li { display: flex; align-items: center; gap: 10px; line-height: 1.45; }
  .contact__list svg { width: 14px; height: 14px; flex: none; fill: var(--ink); }

  .swoosh { position: absolute; left: 0; top: 0; width: 700px; height: 400px; z-index: 1; }
</style>
</head>
<body>
<main class="canvas">
  <section class="card card--front" aria-label="Card front">
    <div class="brand">
      <span class="brand__dot"></span>
      <span class="brand__name"><span class="line1">Brookvale</span><span class="line2">Equipment Services</span></span>
    </div>
  </section>

  <section class="card card--back" aria-label="Card back">
    <svg class="swoosh" viewBox="0 0 700 400" preserveAspectRatio="none" aria-hidden="true">
      <path d="M0 300 C 150 335, 330 345, 480 305 C 570 282, 630 280, 700 272 L700 400 L0 400 Z" fill="var(--mid-grey)"/>
      <path d="M0 316 C 160 348, 340 356, 490 318 C 580 296, 640 294, 700 288 L700 400 L0 400 Z" fill="var(--paper)"/>
      <path d="M0 326 C 170 356, 350 364, 500 328 C 590 306, 645 302, 700 298 L700 400 L0 400 Z" fill="var(--ink)"/>
    </svg>

    <div class="brand">
      <span class="brand__dot"></span>
      <span class="brand__name"><span class="line1">Brookvale</span><span class="line2">Equipment Services</span></span>
    </div>

    <div class="divider"></div>

    <div class="contact">
      <h1 class="contact__name">Dana Whitfield</h1>
      <p class="contact__role">Managing Director</p>
      <p class="contact__address">214 Harlow Mill Road<br>Ashby, CT 06412 USA</p>
      <ul class="contact__list">
        <li><svg viewBox="0 0 16 16"><path d="M2 6c0-2 2-3 6-3s6 1 6 3v1h-3V5.5H5V7H2zM4 8h8l2 6H2z"/></svg>555 214 0870</li>
        <li><svg viewBox="0 0 16 16"><path d="M4 0h8a1 1 0 0 1 1 1v14a1 1 0 0 1-1 1H4a1 1 0 0 1-1-1V1a1 1 0 0 1 1-1zm1 2v10h6V2zm3 11a1 1 0 1 0 0 2 1 1 0 0 0 0-2z"/></svg>555 367 2291</li>
        <li><svg viewBox="0 0 16 16"><path d="M0 3h16v1L8 9 0 4zm0 3 8 5 8-5v7H0z"/></svg>info@brookvale.com</li>
      </ul>
    </div>
  </section>
</main>
</body>
</html>
```